Summer Resolution Do it Now

I run a hypnotherapy practice that helps people
Loose Weight,Stop smoking ,overcome fear of Public speaking and improve Confidence and positive attitude.
I like to market a especific group in the CBD Melbourne as I only practice once a week in the city.

I have some photographs that will go well for the flyer what I am after is something very professional ,sober and elegant.

Target Market(s)

CBD corporate Melbourne market 25 till 60 year old

Industry/Entity Type

Hypnotherapy

Requirements
Must have
• flyer should be two sided , must have http://www.calmtranceclinic.example/ and the phone number 0427916058 and encourage to book online .

```html
<!DOCTYPE html>
<html lang="en">
<head>
<meta charset="utf-8">
<title>Calm Trance Clinic – Two-sided Card</title>
<link href="https://fonts.googleapis.com/css2?family=Barlow+Condensed:wght@700&family=Barlow:wght@400;500;600&family=Noto+Serif:ital,wght@1,700&display=swap" rel="stylesheet">
<style>
  :root {
    --backdrop: #2f3a3c;
    --paper: #f4f5f5;
    --sky: #16b0ec;
    --ink-teal: #1f4a52;
    --white: #ffffff;
    --photo-grey: #b8bec0;
    --photo-warm: #d9cdb4;
    --photo-green: #2f9f68;
  }
  html, body {
    margin: 0;
    padding: 0;
    width: 1200px;
    height: 974px;
    overflow: hidden;
    background: var(--backdrop);
  }
  .canvas {
    position: relative;
    width: 1200px;
    height: 974px;
  }
  .card {
    position: absolute;
    width: 680px;
    height: 410px;
    background: var(--paper);
    box-sizing: border-box;
    padding: 20px;
    box-shadow: 0 6px 18px rgba(0,0,0,.35);
  }
  .card--front { left: 90px; top: 64px; }
  .card--back { left: 430px; top: 500px; }

  .card__face {
    position: relative;
    width: 100%;
    height: 100%;
    overflow: hidden;
  }

  /* Front */
  .photo-area {
    position: absolute;
    inset: 0;
    background:
      radial-gradient(ellipse 38% 70% at 70% 35%, var(--photo-warm) 0%, rgba(217,205,180,0) 70%),
      linear-gradient(180deg, rgba(47,159,104,0) 55%, rgba(47,159,104,.9) 100%),
      linear-gradient(90deg, var(--photo-grey) 0%, #c6c9c4 45%, #cfc4ad 70%, #a9b7a6 100%);
  }
  .benefits {
    position: absolute;
    left: 34px;
    top: 40px;
    margin: 0;
    padding: 0;
    list-style: none;
    font-family: "Barlow Condensed", "Arial Narrow", sans-serif;
    font-weight: 700;
    font-size: 29px;
    line-height: 1.05;
    text-transform: uppercase;
    color: var(--white);
    text-shadow: 2px 2px 0 var(--ink-teal);
    letter-spacing: .5px;
  }
  .benefits li { margin-bottom: 16px; }
  .call-strip {
    position: absolute;
    left: 0;
    top: 300px;
    width: 360px;
    height: 48px;
    background: rgba(245,246,246,.92);
    box-shadow: 0 2px 6px rgba(0,0,0,.15);
    display: flex;
    align-items: center;
    padding-left: 40px;
    box-sizing: border-box;
    font-family: "Noto Serif", Georgia, serif;
    font-style: italic;
    font-weight: 700;
    font-size: 25px;
    color: var(--ink-teal);
  }

  /* Back */
  .card--back .card__face { background: var(--sky); }
  .bookmark {
    position: absolute;
    right: 70px;
    top: -2px;
    width: 140px;
    height: 130px;
  }
  .bookmark__label {
    position: absolute;
    right: 70px;
    top: 28px;
    width: 140px;
    text-align: center;
    font-family: "Noto Serif", Georgia, serif;
    font-style: italic;
    font-weight: 700;
    font-size: 21px;
    line-height: 1.15;
    color: var(--ink-teal);
    text-transform: uppercase;
  }
  .web-address {
    position: absolute;
    left: 8px;
    top: 152px;
    margin: 0;
    font-family: "Barlow", Arial, sans-serif;
    font-weight: 500;
    font-size: 42px;
    color: var(--white);
    letter-spacing: .3px;
  }
  .practitioner {
    position: absolute;
    left: 40px;
    top: 222px;
    font-family: "Barlow", Arial, sans-serif;
    color: var(--white);
  }
  .practitioner__name {
    font-weight: 600;
    font-size: 21px;
    margin: 0;
  }
  .practitioner__role {
    font-weight: 400;
    font-size: 21px;
    margin: 2px 0 0;
  }
</style>
</head>
<body>
<main class="canvas">

  <section class="card card--front" aria-label="Card front">
    <div class="card__face">
      <div class="photo-area" role="img" aria-label="Photograph of a smiling blonde woman in a green shirt, softly blurred office background"></div>
      <ul class="benefits">
        <li>Loose weight</li>
        <li>Improve confidence<br>and positive attitude</li>
        <li>Overcome fear<br>of public speaking</li>
        <li>Stop smoking</li>
      </ul>
      <div class="call-strip">Call now! 0427 916 058</div>
    </div>
  </section>

  <section class="card card--back" aria-label="Card back">
    <div class="card__face">
      <svg class="bookmark" viewBox="0 0 140 130" aria-hidden="true">
        <polygon points="0,0 140,0 140,130 70,96 0,130" fill="#f4f5f5"/>
      </svg>
      <div class="bookmark__label">Book<br>online!</div>
      <p class="web-address">www.calmtranceclinic.example</p>
      <div class="practitioner">
        <p class="practitioner__name">Daniel Whitford</p>
        <p class="practitioner__role">Melbourne Hypnotherapyst</p>
      </div>
    </div>
  </section>

</main>
</body>
</html>
```